New Website for Consulting Company

Our company needs a fresh web design to help us drive our business forward. We are a consulting and software provider to Airports, Air Traffic Organizations, Builders and Architects. We specialize in analyzing operations, monitoring noise levels and creating software to improve operations, meet customer requirements and improve public relations.
Additional Info:
- Additional requirements can be found in the Web Design Brief
- Logo and logo branding attached
Target Market(s)
Airlines, Airports, Government Agencies, and Real Estate Developers
Industry/Entity Type
Aviation
Coding
Coded - Design and coding required
Number of Pages Required
2 page
Colors
Designer to choose colors to be used in the design.
Requirements
Must have
- - Create a Wordpress Design (Coded - Design and coding required)
- - Designer must provide full implementation/coding depending on the platform chosen by the client (i.e. Wordpress theme, HTML/CSS, etc.)
- - This is a multi-page site; Supporting pages can be formatted the same, but links need to be in place
- - Colors used must be grey scale, black or match the logo. It is not necessary to use all the colors in our logo
Should not have
- We are not looking for an overly bright site. While our logo has 5 different colors, it is not necessary to use all of them.

```html
<!DOCTYPE html>
<html lang="en">
<head>
<meta charset="utf-8">
<title>Skyvane International</title>
<link rel="stylesheet" href="https://fonts.googleapis.com/css2?family=Merriweather:wght@400;700&family=Poppins:wght@400;500;600&display=swap">
<style>
:root{
  --blue:#2b6aa3;
  --blue-text:#3f6fa6;
  --ink:#2c2c2c;
  --muted:#8a8a8a;
  --panel:#f7f7f7;
  --white:#ffffff;
  --form-bg:rgba(80,88,104,.82);
  --field:rgba(220,224,232,.72);
}
*{box-sizing:border-box;margin:0;padding:0}
html,body{width:1200px;height:2365px;overflow:hidden;background:var(--white)}
body{position:relative;font-family:"Poppins",sans-serif;color:var(--ink)}
.abs{position:absolute}
.serif{font-family:"Merriweather",serif}

.hero{left:0;top:0;width:1200px;height:520px;
  background:linear-gradient(180deg,#1e3258 0%,#3a5a86 35%,#7f8fa3 62%,#a98a63 80%,#4a3a2c 100%)}
.brand{left:121px;top:38px;font-family:"Merriweather",serif;font-weight:700;font-size:22px;color:var(--white);display:flex;align-items:center;gap:8px}
.brand-dot{width:12px;height:12px;background:var(--white)}
.nav{right:110px;top:44px;display:flex;gap:21px;font-family:"Merriweather",serif;font-size:14.5px;font-weight:700;color:var(--white)}
.hero-title{left:121px;top:218px;font-family:"Merriweather",serif;font-weight:700;font-size:27px;line-height:53px;color:var(--white)}
.btn-outline{left:121px;top:339px;width:230px;height:50px;border:2px solid var(--white);color:var(--white);
  font-family:"Merriweather",serif;font-weight:700;font-size:19px;display:flex;align-items:center;justify-content:center}
.help-form{left:778px;top:117px;width:306px;height:358px;background:var(--form-bg);padding:22px 17px}
.help-form h2{font-family:"Poppins",sans-serif;font-weight:500;font-size:21px;color:var(--white);text-align:center;margin-bottom:16px}
.field{background:var(--field);height:28px;font-size:10px;color:var(--white);padding:6px 8px;margin-bottom:15px}
.field-row{display:flex;gap:10px}.field-row .field{flex:1}
.field.tall{height:48px}
.btn-submit{background:var(--blue);color:var(--white);height:35px;font-size:13px;font-weight:500;display:flex;align-items:center;justify-content:center;margin-top:-2px}

.welcome{left:148px;top:564px;width:916px;height:328px;background:var(--panel)}
.welcome-photo{left:0;top:0;width:440px;height:328px;background:linear-gradient(180deg,#3a3f58 0%,#8a5a4a 50%,#e08a3a 70%,#5a3a2a 100%);
  display:flex;align-items:center;justify-content:center;font-family:"Merriweather",serif;font-size:42px;color:var(--white)}
.welcome-copy{left:470px;top:54px;width:418px;text-align:center}
.welcome-copy h2{font-family:"Merriweather",serif;font-weight:400;font-size:23px;color:var(--blue-text);margin-bottom:14px}
.welcome-copy p{font-size:10.5px;line-height:22px;color:var(--muted);text-align:justify}
.btn-solid{display:inline-block;margin-top:12px;background:var(--blue);color:var(--white);font-family:"Merriweather",serif;font-size:15px;padding:9px 19px}

.section-title{width:1200px;left:0;text-align:center;font-family:"Merriweather",serif;font-size:23px;color:var(--blue-text)}
.lead{left:140px;width:920px;text-align:center;font-size:10.5px;line-height:22px;color:var(--muted)}
.category{width:233px;top:1069px}
.category .photo{height:180px}
.category span{display:block;margin-top:14px;font-family:"Merriweather",serif;font-size:19px;color:var(--blue-text)}

.blog{left:0;top:1325px;width:1200px;height:580px;background:var(--panel)}
.blog-main{left:121px;top:1418px;width:608px;height:272px;background:linear-gradient(180deg,#cfd9e6 0%,#9fb3cc 55%,#6f87a8 100%)}
.blog-side-a{left:753px;top:1418px;width:336px;height:179px;background:linear-gradient(180deg,#b89a8a 0%,#7a6a70 55%,#2e2a30 100%)}
.blog-side-b{left:753px;top:1690px;width:336px;height:180px;background:linear-gradient(180deg,#dfe6ee 0%,#b8c4d2 60%,#8a96a6 100%)}
.blog-title{left:121px;top:1706px;width:608px;text-align:center;font-size:13.5px;font-weight:500;color:var(--ink)}
.blog-text{left:128px;top:1740px;width:594px;text-align:center;font-size:10px;line-height:22px;color:var(--muted)}
.read-more{left:387px;top:1853px;font-size:10.5px;color:var(--ink);border-bottom:1px solid var(--ink)}
.side-text{left:763px;top:1610px;width:316px;text-align:center;font-size:10px;line-height:22px;color:var(--muted)}

.testi-title{left:0;width:1200px;top:1950px;text-align:center;font-family:"Merriweather",serif;font-weight:700;font-size:20px;color:var(--ink)}
.quote{width:300px;text-align:center}
.quote svg{display:block;margin:0 auto 14px}
.quote p{font-size:10.5px;line-height:21px;color:var(--muted)}
.quote b{display:block;margin-top:10px;font-weight:400;font-size:15px;color:var(--ink)}

.footer{left:0;top:2258px;width:1200px;height:107px;background:var(--blue)}
.social{left:0;width:1200px;top:28px;display:flex;justify-content:center;gap:40px;font-family:"Merriweather",serif;font-weight:700;font-size:24px;color:var(--white)}
.copyright{left:0;width:1200px;top:80px;text-align:center;font-family:"Merriweather",serif;font-size:10.5px;color:var(--white)}
</style>
</head>
<body>

<header class="abs hero" role="img" aria-label="Airliner landing at dusk over blurred runway lights"></header>
<div class="abs brand"><span class="brand-dot"></span>Skyvane International</div>
<nav class="abs nav"><span>Home</span><span>Airports</span><span>Airspace</span><span>Emissions</span><span>Acoustics</span><span>Visualization</span><span>About</span><span>Contact</span></nav>
<h1 class="abs hero-title">We Provides Consulting, Support Services<br>&amp; Airspace Visualization</h1>
<div class="abs btn-outline">Request A Demo</div>

<form class="abs help-form">
  <h2>How Can We Help?</h2>
  <div class="field-row"><div class="field">First Name</div><div class="field">Last Name</div></div>
  <div class="field">Email</div>
  <div class="field">Phone Number</div>
  <div class="field">How did you hear about us?</div>
  <div class="field tall">Comments</div>
  <div class="btn-submit">Contact Us Today</div>
</form>

<section class="abs welcome">
  <div class="abs welcome-photo" role="img" aria-label="Airliner climbing against an orange sunset sky">WELCOME</div>
  <div class="abs welcome-copy">
    <h2>Aviation .&nbsp; Technology&nbsp; . Visualized</h2>
    <p>Skyvane International invents and deploys innovative management and technology solutions that address complex noise and airspace issues for airports and residential communities. With more than two decades of experience and original software solutions, the company identifies problems precisely and solves them through a diagnostic process that mitigates political, community and technical concerns, and builds consensus for ideas and solutions.</p>
    <span class="btn-solid">CONTACT US TODAY</span>
  </div>
</section>

<h2 class="abs section-title" style="top:935px">Our 4 Primary Categories of Operations</h2>
<p class="abs lead" style="top:985px">Skyvane International is an industry leader in modeling flight procedures that utilize advanced 3D navigation. The 3D visualization of Skyvane's graphics is through VectorSky. VectorSky is Skyvane's cornerstone software &amp; is capable of tracking aircraft movements in 3D by modeling airspace procedures and aircraft emissions in a terminal area or from gate-to-gate, in real time, playback or through the creation of custom 3D videos..</p>

<div class="abs category" style="left:121px"><div class="photo" role="img" aria-label="Airliner parked at an airport gate at sunset" style="background:linear-gradient(180deg,#e8a23a,#b8782a 60%,#4a3a2a)"></div><span style="margin-top:6px">Airports</span></div>
<div class="abs category" style="left:367px"><div class="photo" role="img" aria-label="Rendered aircraft on a lit runway in software" style="background:linear-gradient(180deg,#1a3a44,#2e6a70 55%,#0e1e24)"></div><span>Software</span></div>
<div class="abs category" style="left:612px"><div class="photo" role="img" aria-label="Noise measurement line graph on a screen" style="background:linear-gradient(180deg,#3a3a3a,#1e1e1e)"></div><span>Noise &amp; Emissions</span></div>
<div class="abs category" style="left:858px"><div class="photo" role="img" aria-label="3D visualization of a coastal platform and water" style="background:linear-gradient(180deg,#b8d8ec,#3a9ad8 55%,#1a7ac8)"></div><span>Visualization</span></div>

<section class="abs blog"></section>
<h2 class="abs section-title" style="top:1357px">Check Out Our Blog</h2>
<div class="abs blog-main" role="img" aria-label="Airliner on a snowy apron under a bright sky"></div>
<h3 class="abs blog-title">Lorem Ipsum is simply dummy text of the printing and typesetting industry</h3>
<p class="abs blog-text">Lorem Ipsum is simply dummy text of the printing and typesetting industry. Lorem Ipsum has been the industry's standard dummy text ever since the 1500s, when an unknown printer took a galley of type and scrambled it to make a type specimen book. It has survivedc. Lorem ipsum is simply dummy text of the printing and typesetting industry. Lorem Ipsum has been the industry's standard dummy text ever since the 1500s, when an unknown printer took a galley of type and scrambled it to make a type specimen book. It has survivedc</p>
<span class="abs read-more">Read More &gt;&gt;</span>
<div class="abs blog-side-a" role="img" aria-label="Traveller silhouette in an airport lounge at sunset"></div>
<p class="abs side-text">Lorem Ipsum is simply dummy text of the printing and typesetting industry. Lorem Ipsum has been the industry's standard dummy text ever since the 1500s,</p>
<div class="abs blog-side-b" role="img" aria-label="Traveller silhouette with suitcase by terminal windows"></div>

<h2 class="abs testi-title">What Our Client Say’s About Us</h2>
<p class="abs lead" style="top:1992px;left:290px;width:620px">Lorem Ipsum is simply dummy text of the printing and typesetting industry. Lorem Ipsum has been the industry's standard dummy text ever since the 1500sLorem Ipsum is simply dummy text of the printing and typesetting.</p>

<div class="abs quote" style="left:117px;top:2080px">
  <svg width="20" height="16" viewBox="0 0 20 16"><path fill="#9a9a9a" d="M0 16V9C0 4 2 1 7 0v3C4 4 4 6 4 8h4v8zM11 16V9c0-5 2-8 7-9v3c-3 1-3 3-3 5h4v8z"/></svg>
  <p>Lorem ipsum is simply dummy text of the printing and typesetting industry. Lorem Ipsum has been the ind ustry's standard dummy text</p><b>- Nora Pell</b></div>
<div class="abs quote" style="left:460px;top:2077px">
  <svg width="20" height="16" viewBox="0 0 20 16"><path fill="#9a9a9a" d="M0 16V9C0 4 2 1 7 0v3C4 4 4 6 4 8h4v8zM11 16V9c0-5 2-8 7-9v3c-3 1-3 3-3 5h4v8z"/></svg>
  <p>Lorem ipsum is simply dummy text of the printing and typesetting industry. Lorem Ipsum has been the ind ustry's standard dummy text</p><b style="margin-top:14px">- Owen Marsh</b></div>
<div class="abs quote" style="left:800px;top:2080px">
  <svg width="20" height="16" viewBox="0 0 20 16"><path fill="#9a9a9a" d="M0 16V9C0 4 2 1 7 0v3C4 4 4 6 4 8h4v8zM11 16V9c0-5 2-8 7-9v3c-3 1-3 3-3 5h4v8z"/></svg>
  <p>Lorem ipsum is simply dummy text of the printing and typesetting industry. Lorem Ipsum has been the ind ustry's standard dummy text</p><b>- Lena Cartwright</b></div>

<footer class="abs footer">
  <div class="abs social"><span>Linkline</span><span>Chirper</span></div>
  <p class="abs copyright">©2017 Skyvane International. All Rights Reserved</p>
</footer>

</body>
</html>
```